Business Card Design Project

Business card design for an IT Service company. A logo has already been created in a different contest and has been attached to this project. Ideally we're looking for a double sided business card that matches the look and feel of our newly created logo.

We're open to creativity if you feel a tag line is needed such as "IT Services and Application Development". We're open to really and look and feel - even single sided business cards if you feel you have something that's a great idea.

Last thought here - I'm not sure how it'll look but maybe a two tone card? One side dark blue and the other side white? Don't limit the design submissions to this tho - just curious if it would look good

Nothing too busy please - simple... Thank you and happy designing!

Target Market(s)

Businesses that require IT Services and support for hosted services, technical consultation, web design.

Industry/Entity Type

Business

Font styles to use
Sans Serif

Requirements
Must have
• Use the colors provided in the logo (see attachment) or additional colors that compliment
Must have the following contact info (not necessarily in this order):
- Alan Fisk
- Founding Partner
- afisk@quillbarrow.example
- 555-382-1946
- www.quillbarrow.example

```html
<!DOCTYPE html>
<html lang="en">
<head>
<meta charset="utf-8">
<title>QuillBarrow Business Card</title>
<link rel="stylesheet" href="https://fonts.googleapis.com/css2?family=Pathway+Gothic+One&family=Source+Sans+3:wght@400;600;700&display=swap">
<style>
  :root {
    --backdrop: #000000;
    --card: #ffffff;
    --green: #43ae4f;
    --blue: #0c6aa8;
    --slate: #50546e;
    --name-green: #17963a;
    --ink: #2b2b2b;
    --navy: #1b2a4e;
  }
  * { margin: 0; padding: 0; box-sizing: border-box; }
  html, body {
    width: 1200px; height: 900px; overflow: hidden;
    background: var(--backdrop);
    font-family: "Source Sans 3", sans-serif;
  }
  .card {
    position: absolute; left: 125px; top: 165px;
    width: 950px; height: 570px;
    background: var(--card);
    overflow: hidden;
  }
  .stripe { position: absolute; top: 0; height: 100%; }
  .stripe--green { left: 0; width: 37px; background: var(--green); }
  .stripe--blue { left: 37px; width: 32px; background: var(--blue); }
  .stripe--slate { left: 69px; width: 28px; background: var(--slate); }

  .identity { position: absolute; left: 145px; top: 138px; }
  .identity__name {
    font-family: "Pathway Gothic One", sans-serif;
    font-size: 40px; line-height: 1; color: var(--name-green);
    font-weight: 400;
  }
  .identity__role {
    margin-top: 8px; font-size: 21px; color: var(--ink);
  }

  .contacts { position: absolute; left: 80px; top: 299px; list-style: none; }
  .contact {
    display: flex; align-items: center; height: 32px; margin-bottom: 12.5px;
    font-size: 18px; color: var(--ink);
  }
  .contact__icon {
    width: 32px; height: 32px; flex: none; margin-right: 13px;
  }

  .brand { position: absolute; left: 490px; top: 340px; }
  .brand__row { display: flex; align-items: center; gap: 14px; }
  .brand__mark { width: 40px; height: 40px; background: var(--navy); }
  .brand__name {
    font-size: 54px; font-weight: 700; color: var(--navy); line-height: 1;
    letter-spacing: -0.5px;
  }
  .brand__tagline {
    margin-top: 8px; font-size: 18.5px; color: var(--ink);
  }
</style>
</head>
<body>
  <main class="card">
    <div class="stripe stripe--green"></div>
    <div class="stripe stripe--blue"></div>
    <div class="stripe stripe--slate"></div>

    <header class="identity">
      <h1 class="identity__name">Alan Fisk</h1>
      <p class="identity__role">Founding Partner</p>
    </header>

    <ul class="contacts">
      <li class="contact">
        <svg class="contact__icon" viewBox="0 0 32 32" aria-hidden="true">
          <circle cx="16" cy="16" r="15" fill="#50546e" stroke="#fff" stroke-width="2"/>
          <path d="M16 7a6 6 0 0 0-6 6c0 4.5 6 12 6 12s6-7.5 6-12a6 6 0 0 0-6-6z" fill="#fff"/>
          <circle cx="16" cy="13" r="2.3" fill="#50546e"/>
        </svg>
        418 Harlow Street, Brookfield 60213
      </li>
      <li class="contact">
        <svg class="contact__icon" viewBox="0 0 32 32" aria-hidden="true">
          <circle cx="16" cy="16" r="15" fill="#50546e" stroke="#fff" stroke-width="2"/>
          <path d="M8 13c0-2 3.5-3.5 8-3.5s8 1.5 8 3.5v1.5h-3.5v-2h-9v2H8z" fill="#fff"/>
          <rect x="10" y="15.5" width="12" height="7" rx="1" fill="#fff"/>
          <circle cx="16" cy="19" r="1.6" fill="#50546e"/>
        </svg>
        555-382-1946
      </li>
      <li class="contact">
        <svg class="contact__icon" viewBox="0 0 32 32" aria-hidden="true">
          <circle cx="16" cy="16" r="15" fill="#50546e" stroke="#fff" stroke-width="2"/>
          <rect x="8.5" y="10.5" width="15" height="11" fill="none" stroke="#fff" stroke-width="1.5"/>
          <path d="M8.5 10.5l7.5 6.5 7.5-6.5" fill="none" stroke="#fff" stroke-width="1.5"/>
        </svg>
        afisk@quillbarrow.example
      </li>
      <li class="contact">
        <svg class="contact__icon" viewBox="0 0 32 32" aria-hidden="true">
          <circle cx="16" cy="16" r="15" fill="#50546e" stroke="#fff" stroke-width="2"/>
          <g fill="none" stroke="#fff" stroke-width="2" stroke-linecap="round">
            <path d="M14.5 17.5l3-3"/>
            <path d="M13 15l-2.5 2.5a2.5 2.5 0 0 0 3.5 3.5L16.5 18.5"/>
            <path d="M19 17l2.5-2.5a2.5 2.5 0 0 0-3.5-3.5L15.5 13.5"/>
          </g>
        </svg>
        www.quillbarrow.example
      </li>
    </ul>

    <section class="brand">
      <div class="brand__row">
        <span class="brand__mark"></span>
        <span class="brand__name">QuillBarrow</span>
      </div>
      <p class="brand__tagline">IT Services and Application Development</p>
    </section>
  </main>
</body>
</html>
```